Change the world and help build SpinLOOM.tv!

We need a mobile website design for our Beta release - see wireframes attached.
See our Logo design files attached along with fonts, etc.
Please see enclosed .PDF that provides a great overview of our company, LOOM.
Any questions, feel free to ask - we're very engaged here on Sketch Hive and will make ourselves available.
Thanks!
Tobias
Updates
Very pleased with what's coming in! Would like to see some more variety and more volume of designs.
Target Market(s)
Ages 13+ (all genders, races, creeds, income levels, etc)
Coding
Coded - Design and coding required
Number of Pages Required
5+ page
Font styles to use
Colors
Designer to choose colors to be used in the design.
Look and feel
Each slider illustrates characteristics of the customer's brand and the style your logo design should communicate.

```html
<!DOCTYPE html>
<html lang="en">
<head>
<meta charset="utf-8">
<title>SpinLOOM.tv – Beta mobile screens</title>
<link href="https://fonts.googleapis.com/css2?family=Bebas+Neue&family=Lato:wght@400;700&display=swap" rel="stylesheet">
<style>
:root{
  --stage:#63b6d2;
  --brand-blue:#62b3d1;
  --navy:#0d2455;
  --white:#ffffff;
  --ink:#3d4a5c;
  --field:rgba(255,255,255,.72);
  --panel:rgba(255,255,255,.45);
  --grass-top:#7fb9c9;
  --grass-bottom:#6aa79a;
}
*{box-sizing:border-box;margin:0;padding:0}
html,body{width:1200px;height:468px;overflow:hidden}
body{background:var(--stage);font-family:"Lato",sans-serif;color:var(--ink);display:flex;justify-content:center;align-items:center;gap:90px}
.screen{width:210px;height:440px;border-radius:26px;overflow:hidden;position:relative;background:var(--white)}
.status{height:22px;display:flex;justify-content:space-between;align-items:center;padding:0 18px;font-size:7px;color:var(--navy)}
.status-icons{display:flex;gap:3px;align-items:center}
.wordmark{font-family:"Lato",sans-serif;font-weight:700;color:var(--navy);line-height:1.1}
.tagline{font-family:"Lato",sans-serif;font-weight:400;font-size:6px;color:var(--ink);margin-top:3px}
.footer-links{display:flex;justify-content:center;gap:5px;font-size:4.6px;color:var(--navy)}
.footer-links span+span::before{content:"|";margin-right:5px}

/* Landing screen */
.landing-header{display:flex;justify-content:space-between;align-items:center;padding:4px 12px 8px}
.landing-header .wordmark{font-size:12px}
.header-actions{display:flex;gap:4px}
.pill{font-size:4.8px;font-weight:700;color:var(--white);border-radius:8px;padding:3px 6px;text-transform:uppercase;white-space:nowrap}
.pill-beta{background:var(--brand-blue)}
.pill-influencer{background:var(--navy)}
.hero-photo{height:150px;background:linear-gradient(160deg,#5d7f9c 0%,#6f8d7a 55%,#5b7a4c 100%);display:flex;align-items:center;justify-content:center}
.donate-band{padding:14px 12px 10px}
.donate-button{background:var(--brand-blue);color:var(--white);font-family:"Bebas Neue",sans-serif;font-size:13px;letter-spacing:.5px;border-radius:14px;height:28px;display:flex;align-items:center;justify-content:center}
.landing .footer-links{margin-top:8px}

/* Signup screen */
.signup{background:linear-gradient(180deg,#86c3d6 0%,var(--grass-top) 45%,var(--grass-bottom) 100%)}
.signup-photo{position:absolute;inset:0;background:linear-gradient(180deg,rgba(120,190,214,.9) 0%,rgba(110,178,190,.55) 50%,rgba(106,167,140,.6) 100%)}
.signup-content{position:relative;padding:0 12px;text-align:center}
.brand-block{margin-top:10px}
.signup .wordmark{font-size:20px}
.signup .tagline{color:var(--white)}
.intro{font-size:5.6px;line-height:1.6;color:var(--white);margin-top:8px}
.form-panel{background:var(--panel);border-radius:12px;padding:10px 8px;margin-top:10px;display:flex;flex-direction:column;gap:6px}
.field{height:20px;border-radius:10px;background:var(--field);display:flex;align-items:center;gap:8px;padding-left:2px;font-size:5.4px;color:#8a98a8}
.field-icon{width:16px;height:16px;border-radius:50%;background:var(--brand-blue);display:flex;align-items:center;justify-content:center}
.story{height:52px;border-radius:10px;background:var(--field);font-size:5.4px;color:#8a98a8;text-align:left;padding:8px 10px}
.register{margin-top:10px;height:21px;border-radius:11px;background:var(--navy);color:var(--white);font-family:"Bebas Neue",sans-serif;font-size:10px;letter-spacing:.5px;display:flex;align-items:center;justify-content:center}
.signup .footer-links{margin-top:12px;color:var(--white)}
.signup .status{color:var(--white)}

/* Thank-you screen */
.thanks-header{text-align:center;padding:10px 12px 12px}
.thanks-header .wordmark{font-size:17px}
.thanks-band{background:var(--brand-blue);color:var(--white);text-align:center;padding:16px 16px 14px}
.thanks-title{font-family:"Bebas Neue",sans-serif;font-weight:400;font-size:16px;letter-spacing:.4px;color:var(--navy)}
.thanks-copy{font-size:5.6px;line-height:1.6;margin-top:8px}
.sign-off{font-size:5.6px;margin-top:8px}
.signature{font-family:"Bebas Neue",sans-serif;font-size:10px;color:var(--navy);margin-top:3px;letter-spacing:.4px}
.thanks .footer-links{margin-top:10px}
</style>
</head>
<body>

<section class="screen landing">
  <div class="status"><span>9:41</span><span class="status-icons"><svg width="10" height="6"><rect x="0" y="4" width="2" height="2" fill="#0d2455"/><rect x="3" y="2.5" width="2" height="3.5" fill="#0d2455"/><rect x="6" y="1" width="2" height="5" fill="#0d2455"/></svg><svg width="11" height="6"><rect x=".5" y=".5" width="9" height="5" rx="1" fill="none" stroke="#0d2455"/><rect x="1.5" y="1.5" width="6" height="3" fill="#0d2455"/></svg></span></div>
  <header class="landing-header">
    <div class="wordmark">SpinLOOM.tv</div>
    <div class="header-actions"><span class="pill pill-beta">Join Beta</span><span class="pill pill-influencer">Influencer Sign Up</span></div>
  </header>
  <div class="hero-photo" role="img" aria-label="Video still of children running through a grassy field">
    <svg width="34" height="34" viewBox="0 0 34 34"><circle cx="17" cy="17" r="15" fill="none" stroke="#fff" stroke-width="1.6"/><path d="M13 10 L24 17 L13 24 Z" fill="none" stroke="#fff" stroke-width="1.6" stroke-linejoin="round"/></svg>
  </div>
  <div class="donate-band">
    <div class="donate-button">Donate to our FundSpark campaign!</div>
    <nav class="footer-links"><span>Terms and Conditions</span><span>Privacy Policy</span><span>About LOOM</span><span>The LOOM Team</span></nav>
  </div>
</section>

<section class="screen signup">
  <div class="signup-photo" role="img" aria-label="Tinted photo of children playing outdoors in a meadow"></div>
  <div class="signup-content">
    <div class="status"><span>9:41</span><span class="status-icons"><svg width="10" height="6"><rect x="0" y="4" width="2" height="2" fill="#fff"/><rect x="3" y="2.5" width="2" height="3.5" fill="#fff"/><rect x="6" y="1" width="2" height="5" fill="#fff"/></svg><svg width="11" height="6"><rect x=".5" y=".5" width="9" height="5" rx="1" fill="none" stroke="#fff"/><rect x="1.5" y="1.5" width="6" height="3" fill="#fff"/></svg></span></div>
    <div class="brand-block">
      <div class="wordmark">SpinLOOM.tv</div>
      <div class="tagline">Calm Together</div>
    </div>
    <p class="intro">Sing-up to receive an invitation to join our pre-launch (Beta) version of LOOM! Join our growing community of mental health warriors and help build a platform that can improve the lives of millions of people.</p>
    <form class="form-panel">
      <div class="field"><span class="field-icon"><svg width="8" height="8" viewBox="0 0 8 8"><circle cx="4" cy="2.5" r="1.7" fill="#fff"/><path d="M1 8 a3 3 0 0 1 6 0 Z" fill="#fff"/></svg></span>Name</div>
      <div class="field"><span class="field-icon"><svg width="8" height="8" viewBox="0 0 8 8"><rect x="1" y="1.5" width="6" height="5.5" rx=".6" fill="none" stroke="#fff" stroke-width=".9"/><line x1="1" y1="3.3" x2="7" y2="3.3" stroke="#fff" stroke-width=".9"/></svg></span>Date of Birth</div>
      <div class="field"><span class="field-icon"><svg width="8" height="8" viewBox="0 0 8 8"><path d="M4 7.5 C2 5 1.5 4 1.5 3 a2.5 2.5 0 0 1 5 0 C6.5 4 6 5 4 7.5 Z" fill="none" stroke="#fff" stroke-width=".9"/><circle cx="4" cy="3" r=".9" fill="#fff"/></svg></span>Address</div>
      <div class="field"><span class="field-icon"><svg width="8" height="8" viewBox="0 0 8 8"><rect x=".8" y="1.8" width="6.4" height="4.4" fill="none" stroke="#fff" stroke-width=".9"/><path d="M.8 1.8 L4 4.4 L7.2 1.8" fill="none" stroke="#fff" stroke-width=".9"/></svg></span>Email</div>
      <div class="field"><span class="field-icon"><svg width="8" height="8" viewBox="0 0 8 8"><rect x="2.3" y=".8" width="3.4" height="6.4" rx=".6" fill="none" stroke="#fff" stroke-width=".9"/><circle cx="4" cy="6" r=".4" fill="#fff"/></svg></span>Phone</div>
      <div class="story">Share Your Story With Us!</div>
    </form>
    <div class="register">Register</div>
    <nav class="footer-links"><span>Terms and Conditions</span><span>Privacy Policy</span><span>About LOOM</span><span>The LOOM Team</span></nav>
  </div>
</section>

<section class="screen thanks">
  <div class="status"><span>9:41</span><span class="status-icons"><svg width="10" height="6"><rect x="0" y="4" width="2" height="2" fill="#0d2455"/><rect x="3" y="2.5" width="2" height="3.5" fill="#0d2455"/><rect x="6" y="1" width="2" height="5" fill="#0d2455"/></svg><svg width="11" height="6"><rect x=".5" y=".5" width="9" height="5" rx="1" fill="none" stroke="#0d2455"/><rect x="1.5" y="1.5" width="6" height="3" fill="#0d2455"/></svg></span></div>
  <header class="thanks-header">
    <div class="wordmark">SpinLOOM.tv</div>
    <div class="tagline">Calm Together</div>
  </header>
  <div class="thanks-band">
    <h1 class="thanks-title">Thank you for signing up!</h1>
    <p class="thanks-copy">Please check your email for a confirmation and your Beta invitation, which will arrive soon.</p>
    <p class="thanks-copy">We are excited to have you on the LOOM team! You're doing a wonderful thing for the world, and we are grateful for you!</p>
    <p class="sign-off">With love,</p>
    <p class="signature">Mara &amp; Tobias</p>
  </div>
  <nav class="footer-links"><span>Terms and Conditions</span><span>Privacy Policy</span><span>About LOOM</span><span>The LOOM Team</span></nav>
</section>

</body>
</html>
```